BrivoPeak Business Card Design Project

We are looking for a modern, clean business card design for our new company. We are a consulting firm focused on the financial services market providing management and IT consulting to banks, insurance companies, etc. Please include our company logo and company contact information from the attached file in the design. Two versions of the logo are attached, either version is acceptable. Logos are available in other file formats if needed. We would like to include the contact information for both our UK and US offices as well as the following information for each individual card holder: Name, position/title, address, phone number and e-mail address.
Updates
Project Deadline Extended
Reason: A last minute trip over seas has prevented us from finalizing the decision. A decision will be made this week. We apologize for the inconvenience.
Industry/Entity Type
Business
Contact Information for Business Card
Company logo.
Company locations and phone numbers for both the US and UK offices.
Company URL.
Cardholder Name
Cardholder Position/title
Cardholder Address
Cardholder Phone Number
Cardholder e-mail Address
Look and feel
Each slider illustrates characteristics of the customer's brand and the style your logo design should communicate.

```html
<!DOCTYPE html>
<html lang="en">
<head>
<meta charset="utf-8">
<title>BrivoPeak Partners – Business Card</title>
<link rel="stylesheet" href="https://fonts.googleapis.com/css2?family=Open+Sans:wght@400;600;700&display=swap">
<style>
  :root {
    --navy: #1f3764;
    --navy-deep: #2a3a57;
    --grey: #7a7a7a;
    --ink: #1d1d1d;
    --paper: #ffffff;
    --backdrop: #e8e5e0;
  }
  * { margin: 0; padding: 0; box-sizing: border-box; }
  html, body {
    width: 1200px; height: 902px; overflow: hidden;
    background: var(--backdrop);
    font-family: "Open Sans", sans-serif;
  }
  .sheet {
    width: 1200px; height: 902px;
    display: flex; flex-direction: column; align-items: center; justify-content: center;
    gap: 44px;
  }
  .card {
    position: relative;
    width: 620px; height: 354px;
    border-radius: 4px;
    overflow: hidden;
    box-shadow: 0 6px 18px rgba(0,0,0,0.18);
  }
  .card--front { background: var(--paper); }
  .card--back {
    background: var(--navy-deep);
    display: flex; align-items: center; justify-content: center;
  }
  .swoosh { position: absolute; inset: 0; }
  .brand {
    position: absolute; left: 16px; top: 118px; width: 270px;
    display: flex; align-items: center; justify-content: center; gap: 10px;
  }
  .brand__mark { width: 18px; height: 18px; background: var(--navy); flex: none; }
  .brand__name {
    font-weight: 700; font-size: 26px; color: var(--navy); letter-spacing: -0.3px;
    white-space: nowrap;
  }
  .brand--reverse .brand__mark { background: var(--paper); }
  .brand--reverse .brand__name { color: var(--paper); font-size: 38px; }
  .brand--reverse { position: static; width: auto; gap: 14px; }
  .divider {
    position: absolute; left: 298px; top: 28px; width: 1px; height: 210px;
    background: var(--ink);
  }
  .holder { position: absolute; left: 322px; top: 26px; }
  .holder__name { font-size: 26px; font-weight: 400; color: var(--navy); line-height: 1.1; }
  .holder__title { font-size: 15px; font-weight: 600; color: var(--ink); margin-top: 4px; }
  .contacts {
    position: absolute; left: 322px; top: 104px;
    list-style: none; font-size: 13.5px; color: var(--ink);
  }
  .contacts li { display: flex; align-items: flex-start; gap: 9px; line-height: 21px; }
  .contacts svg { flex: none; margin-top: 4px; }
  .office-line {
    fill: var(--paper); font-size: 13px; font-family: "Open Sans", sans-serif;
  }
</style>
</head>
<body>
<main class="sheet">
  <section class="card card--front" aria-label="Card front">
    <svg class="swoosh" width="620" height="354" viewBox="0 0 620 354" aria-hidden="true">
      <path d="M620 232 Q 430 290 140 330" fill="none" stroke="var(--grey)" stroke-width="8" stroke-linecap="round"/>
      <path d="M0 354 L0 330 Q 330 318 620 250 L620 354 Z" fill="var(--navy)"/>
      <path id="address-path" d="M50 348 Q 330 324 612 268" fill="none"/>
      <text class="office-line"><textPath href="#address-path">48 Cedar Bend Ave, Suite 210 Millbrook UT 84000 United States</textPath></text>
    </svg>

    <div class="brand">
      <span class="brand__mark"></span>
      <span class="brand__name">BrivoPeak Partners</span>
    </div>

    <div class="divider"></div>

    <div class="holder">
      <p class="holder__name">Owen Hartley</p>
      <p class="holder__title">Managing Director</p>
    </div>

    <ul class="contacts">
      <li>
        <svg width="13" height="13" viewBox="0 0 13 13"><rect width="13" height="13" rx="2" fill="var(--ink)"/><path d="M3 4.5 Q6.5 2 10 4.5 L9 6 L4 6 Z M4 7 H9 V10 H4 Z" fill="#fff"/></svg>
        <span>US: (555) 014-2270</span>
      </li>
      <li>
        <svg width="13" height="13" viewBox="0 0 13 13"><rect width="13" height="13" rx="2" fill="var(--ink)"/><path d="M3 4.5 Q6.5 2 10 4.5 L9 6 L4 6 Z M4 7 H9 V10 H4 Z" fill="#fff"/></svg>
        <span>UK: +44 7700 900412</span>
      </li>
      <li>
        <svg width="13" height="13" viewBox="0 0 13 13"><rect width="13" height="13" rx="2" fill="var(--ink)"/><circle cx="6.5" cy="6.5" r="3.6" fill="none" stroke="#fff" stroke-width="1.2"/><path d="M2.9 6.5 H10.1 M6.5 2.9 V10.1" stroke="#fff" stroke-width="0.9"/></svg>
        <span>www.brivopeakpartners.com</span>
      </li>
      <li>
        <svg width="13" height="13" viewBox="0 0 13 13"><rect width="13" height="13" rx="2" fill="var(--ink)"/><rect x="2.8" y="4" width="7.4" height="5.2" fill="#fff"/><path d="M2.8 4 L6.5 7 L10.2 4" fill="none" stroke="var(--ink)" stroke-width="0.9"/></svg>
        <span>owen@brivopeakpartners.com</span>
      </li>
      <li>
        <svg width="13" height="13" viewBox="0 0 13 13"><rect width="13" height="13" rx="2" fill="var(--ink)"/><path d="M6.5 10.5 L4 6.5 A2.8 2.8 0 1 1 9 6.5 Z" fill="#fff"/><circle cx="6.5" cy="5.3" r="1" fill="var(--ink)"/></svg>
        <span>14 Fenmore Street London E2<br>9QT Great Britain</span>
      </li>
    </ul>
  </section>

  <section class="card card--back" aria-label="Card back">
    <div class="brand brand--reverse">
      <span class="brand__mark"></span>
      <span class="brand__name">BrivoPeak Partners</span>
    </div>
  </section>
</main>
</body>
</html>
```